Book Cover Design (Front & Back)

I am looking to perfect & improve current design of my Book:

Hear me out, I'm a vendor ...

This book is about the good and the bad way of selling, in short the wolf sells because he is greedy and doesn't care, the dog sells, because he is looking to add value.

I like the current design, it's just that no attention to font and spacing and design elements have been given.

The current size is: 5.5" x 8.5" (13.97 x 21.59 cm)
Updates

Still open to receive concepts, and I will switch to guaranteeing that I will select one ...

Target Market(s)

Sales People, Entrepreneurs, Self-employed

Industry/Entity Type

Sales

Font styles to use
Sans Serif

Colors

Designer to choose colors to be used in the design.

Requirements
Must have
• Must have is:
• - The title: Hear me out, I'm a Vendor
• - the attached badge (idea: like it is stamped on the cover)
• - the subtitle: how you earn profitable customers through trust and value
• - the photo on the back
• - Space for isbn barcodes the back
• - the text (explanation and the piece about the author)
• - the additional mention of 96.000 hours of training, etc.
• THIS WAS THE IDEA I HAD BUT NOW I AM NOT SO SURE:
• The DOG BADGE is now taking too much attention, it would be great to have this badge redesign it into a stamp, as in saying it is quality ... see attachment regarding stamp or make the badge into a wax seal ... that might also be an option
• NEW TEXT FOR ON THE BACK:
• Do you want to be a Sales Wolf or a Prime Pitch Falcon?
• The Sales Wolf desperately chases customers every moment of the day. Sell, sell, sell! Customers are skeptical about the Sales Wolf and will avoid doing business with him as much as possible.
• The Sales Dog has customers waiting on his doorstep, asking to buy, as they are convinced that doing business with the Sales Dog will help them to be more successful and achieve their objectives!
• Apply the right mindset, so that you become the Prime Pitch Falcon in your industry, region, or division by mastering the power of trust and value.
• Marek Oostenbrink is an internationally acclaimed author, speaker, and trainer with over 20 years of sales experience. Marek has trained more than 10,000 sales professionals, transforming them into Prime Pitch Falcons by placing the customer front and center in their buying process.
• Learn more about sales success through trust and value:
• www.primepitchfalcons.com
• www.marekoosten.com
Nice to have
• Good colour
• Nice typography
• Nice spacing
• Great design elements on the back
• PLEASE NOTE: The current quotes are samples, and not real ones (yet)
Should not have
• no other pictures
• or change of texts

```html
<!DOCTYPE html>
<html lang="en">
<head>
<meta charset="utf-8">
<title>Hear me out, I'm a Vendor — Book Cover</title>
<link rel="stylesheet" href="https://fonts.googleapis.com/css2?family=Bebas+Neue&family=Mr+Dafoe&family=Noto+Serif:ital,wght@0,400;0,700;1,400&display=swap">
<style>
  :root {
    --backdrop: #969696;
    --navy: #0a1f3f;
    --quote-mark: #1d2d4a;
    --accent-blue: #3fc1f0;
    --white: #ffffff;
    --author-ink: #264a5c;
    --seal-light: #f0474b;
    --seal-mid: #d8252b;
    --seal-dark: #9c1217;
  }
  * { margin: 0; padding: 0; box-sizing: border-box; }
  html, body {
    width: 845px; height: 1200px; overflow: hidden;
    background: var(--backdrop);
  }
  .cover {
    position: absolute; left: 96px; top: 98px;
    width: 651px; height: 1006px;
    background: var(--navy);
    overflow: hidden;
  }
  .endorsement {
    position: absolute; left: 0; top: 48px; width: 100%;
    text-align: center;
  }
  .endorsement__mark {
    position: absolute; top: 8px;
    font-family: "Noto Serif", serif; font-weight: 700;
    font-size: 118px; line-height: 1; color: var(--quote-mark);
  }
  .endorsement__mark--open { left: 122px; }
  .endorsement__mark--close { left: 452px; }
  .endorsement__text {
    position: relative;
    font-family: "Noto Serif", serif; font-style: italic;
    font-size: 20px; line-height: 29px; color: var(--white);
  }
  .endorsement__rule {
    width: 56px; height: 2px; background: var(--accent-blue);
    margin: 13px auto 9px;
  }
  .endorsement__name {
    font-family: "Noto Serif", serif; font-size: 16px;
    color: var(--accent-blue);
  }
  .title {
    position: absolute; left: 86px; width: 464px; top: 200px; height: 240px;
    font-weight: 400;
  }
  .title__bold {
    position: absolute; font-family: "Bebas Neue", sans-serif;
    color: var(--white); line-height: 1; white-space: nowrap;
  }
  .title__bold--top { left: 0; top: -10px; font-size: 146px; letter-spacing: 1px; }
  .title__bold--bottom { right: 0; top: 151px; font-size: 84px; letter-spacing: 2px; }
  .title__script {
    position: absolute; font-family: "Mr Dafoe", cursive;
    color: var(--accent-blue); line-height: 1; white-space: nowrap;
  }
  .title__script--top { right: 0; top: 8px; font-size: 94px; }
  .title__script--bottom { right: 246px; top: 140px; font-size: 90px; }
  .title__rule {
    position: absolute; left: 0; top: 131px; width: 464px; height: 4px;
    background: var(--white);
  }
  .seal {
    position: absolute; left: 210px; top: 482px;
    width: 232px; height: 192px;
  }
  .subtitle {
    position: absolute; left: 0; top: 718px; width: 100%;
    text-align: center; font-family: "Noto Serif", serif;
    font-weight: 400;
    font-size: 27px; line-height: 40px; color: var(--white);
    text-transform: uppercase;
  }
  .subtitle strong { font-weight: 700; }
  .author-band {
    position: absolute; left: 0; top: 896px; width: 100%; height: 110px;
    background: var(--white);
    display: flex; align-items: center; justify-content: center;
  }
  .author-band__name {
    font-family: "Noto Serif", serif; font-size: 22px; font-weight: 400;
    color: var(--author-ink); letter-spacing: 0.5px; text-transform: uppercase;
  }
</style>
</head>
<body>
  <main class="cover">
    <section class="endorsement">
      <span class="endorsement__mark endorsement__mark--open">“</span>
      <span class="endorsement__mark endorsement__mark--close">”</span>
      <p class="endorsement__text">Finally a book that shows<br>the heart of selling</p>
      <div class="endorsement__rule"></div>
      <p class="endorsement__name">Pieter K. Lammers</p>
    </section>

    <h1 class="title" aria-label="Hear me out, I'm a Vendor">
      <span class="title__bold title__bold--top">HEAR</span>
      <span class="title__script title__script--top">Me out,</span>
      <span class="title__rule"></span>
      <span class="title__bold title__bold--bottom">A VENDOR</span>
      <span class="title__script title__script--bottom">I’m</span>
    </h1>

    <svg class="seal" viewBox="0 0 232 192" role="img" aria-label="Red wax seal stamped with the customer value badge">
      <defs>
        <radialGradient id="sealTone" cx="45%" cy="40%" r="65%">
          <stop offset="0%" stop-color="var(--seal-light)"/>
          <stop offset="60%" stop-color="var(--seal-mid)"/>
          <stop offset="100%" stop-color="var(--seal-dark)"/>
        </radialGradient>
      </defs>
      <ellipse cx="116" cy="96" rx="115" ry="95" fill="url(#sealTone)"/>
    </svg>

    <h2 class="subtitle">
      How you <strong>earn</strong><br>
      <strong>profitable customers</strong><br>
      through <strong>trust and value</strong>
    </h2>

    <footer class="author-band">
      <p class="author-band__name">By Marek Oostenbrink</p>
    </footer>
  </main>
</body>
</html>
```